Design a poster that illustrates the six central pillars of our school district's efforts with students. The attached PDF outlines the six main competencies we aim for students to possess upon graduation. Each of the 6 has 3 bullet points for the poster as well. The title is "Profile of a Drifter". Our mascot is this attached winged wheel. The overall concept is that staff take kids when they are young and develop these 6 things when they graduate. Our colors are navy, red, and white. We will make this poster in a variety of sizes in offices, classrooms, and in digital spaces as well. On the PDF - ignore the column that says "Synthesis". That has nothing to do with this poster.

The district is Corvath Falls Public Schools https://www.corvath.k12.example.us/

```html
<!DOCTYPE html>
<html lang="en">
<head>
<meta charset="utf-8">
<title>Profile of a Drifter</title>
<link href="https://fonts.googleapis.com/css2?family=Poppins:wght@400;600;700&display=swap" rel="stylesheet">
<style>
  :root {
    --navy: #17173f;
    --red: #a11d23;
    --white: #ffffff;
    --backdrop: #d3d3d3;
    --divider: #c9c9d6;
    --text: #1c1c2e;
  }
  * { box-sizing: border-box; margin: 0; padding: 0; }
  html, body {
    width: 1200px; height: 1000px; overflow: hidden;
    background: var(--backdrop);
    font-family: "Poppins", sans-serif;
  }
  .poster {
    position: absolute; left: 246px; top: 0;
    width: 707px; height: 1000px;
    background: var(--white);
  }
  .poster__title {
    position: absolute; top: 26px; left: 0; width: 100%;
    text-align: center; color: var(--navy);
    font-weight: 700; font-size: 66px; line-height: 1; letter-spacing: -0.5px;
  }
  .poster__subtitle {
    position: absolute; top: 110px; left: 0; width: 100%;
    text-align: center; color: var(--red);
    font-weight: 700; font-size: 25px; line-height: 31px;
  }
  .mascot {
    position: absolute; left: 96px; top: 178px; width: 520px; height: 250px;
    border-radius: 50% / 46%;
    background: radial-gradient(ellipse at center, #2a2a58 0%, #2a2a58 18%, #b8383d 22%, #a11d23 55%, rgba(161,29,35,0.15) 78%, rgba(255,255,255,0) 100%);
  }
  .pillars {
    position: absolute; left: 24px; top: 446px; width: 646px; height: 472px;
    display: grid;
    grid-template-columns: 215px 231px 200px;
    grid-template-rows: 243px 229px;
  }
  .pillar {
    padding: 20px 10px 0 20px;
    text-align: center;
  }
  .pillar:nth-child(3n+2), .pillar:nth-child(3n+3) { border-left: 1.5px solid var(--divider); }
  .pillar:nth-child(-n+3) { border-bottom: 1.5px solid var(--divider); }
  .pillar__icon { width: 56px; height: 56px; display: block; margin: 0 auto; }
  .pillar__icon * { fill: none; stroke: var(--navy); stroke-width: 1.8; stroke-linecap: round; stroke-linejoin: round; }
  .pillar__name {
    margin-top: 18px; color: var(--red);
    font-weight: 600; font-size: 17.5px; line-height: 1.2;
  }
  .pillar__points {
    margin-top: 12px; list-style: none; text-align: left;
  }
  .pillar__points li {
    position: relative; padding-left: 12px; margin-bottom: 10px;
    font-size: 10.3px; line-height: 1.12; color: var(--text);
  }
  .pillar__points li::before {
    content: ""; position: absolute; left: 0; top: 4px;
    width: 3px; height: 3px; border-radius: 50%; background: var(--red);
  }
  .footer {
    position: absolute; left: 0; bottom: 0; width: 100%; height: 49px;
    background: var(--red); color: var(--white);
    display: flex; align-items: center; justify-content: space-between;
    padding: 0 41px; font-size: 14px;
  }
  .footer__district { font-weight: 700; }
  .footer__web { font-weight: 400; }
</style>
</head>
<body>
<main class="poster">
  <h1 class="poster__title">Profile of a Drifter</h1>
  <p class="poster__subtitle">What every Drifter should be<br>when they graduate.</p>
  <div class="mascot" role="img" aria-label="District mascot: a red-winged navy wheel"></div>

  <section class="pillars">
    <article class="pillar">
      <svg class="pillar__icon" viewBox="0 0 56 56"><rect x="20" y="3" width="16" height="11" rx="2"/><path d="M24 7h8M24 10h8"/><circle cx="9" cy="18" r="5"/><circle cx="47" cy="18" r="5"/><circle cx="28" cy="26" r="4"/><path d="M20 38c0-5 4-8 8-8s8 3 8 8"/><circle cx="14" cy="34" r="3.5"/><path d="M6 49c0-5 4-8 8-8s8 3 8 8"/><circle cx="42" cy="34" r="3.5"/><path d="M34 49c0-5 4-8 8-8s8 3 8 8"/></svg>
      <h2 class="pillar__name">Communicator</h2>
      <ul class="pillar__points">
        <li>Expresses ideas clearly and respectfully in writing and speech.</li>
        <li>Listens actively and understands diverse perspectives.</li>
        <li>Adjusts communication to fit audience and context.</li>
      </ul>
    </article>
    <article class="pillar">
      <svg class="pillar__icon" viewBox="0 0 56 56"><path d="M28 10c-9 0-14 6-14 13 0 6 5 9 6 14h16c1-5 6-8 6-14 0-7-5-13-14-13z"/><path d="M28 10v27M21 41h14M22 45h12M25 49h6"/><path d="M28 2v4M42 8l3-3M46 22h5M42 34l3 3"/></svg>
      <h2 class="pillar__name">Critical Thinker</h2>
      <ul class="pillar__points">
        <li>Questions and evaluates information from multiple sources.</li>
        <li>Solves complex problems creatively.</li>
        <li>Uses evidence and diverse viewpoints to make reasoned decisions.</li>
      </ul>
    </article>
    <article class="pillar">
      <svg class="pillar__icon" viewBox="0 0 56 56"><circle cx="28" cy="36" r="12"/><circle cx="28" cy="24" r="4"/><path d="M20 36c0-4 4-6 8-6s8 2 8 6"/><path d="M8 22h8M8 22l3-3M8 22l3 3M48 22h-8M48 22l-3-3M48 22l-3 3M18 4l5 8M18 4v4M18 4h4M38 4l-5 8M38 4v4M38 4h-4"/></svg>
      <h2 class="pillar__name">Responsible</h2>
      <ul class="pillar__points">
        <li>Takes ownership of actions and commitments.</li>
        <li>Manages time, resources, and self to meet expectations.</li>
        <li>Acts with integrity and advocates for self and others.</li>
      </ul>
    </article>
    <article class="pillar">
      <svg class="pillar__icon" viewBox="0 0 56 56"><path d="M16 10a21 21 0 0 1 9-5M31 5a21 21 0 0 1 9 5M47 22a21 21 0 0 1-3 14M36 48a21 21 0 0 1-16 0M11 36a21 21 0 0 1-3-14"/><rect x="25" y="2" width="6" height="6"/><circle cx="49" cy="29" r="3"/><circle cx="28" cy="50" r="3"/><path d="M5 32l3-6 3 6z"/><circle cx="28" cy="23" r="4"/><path d="M20 35c0-5 4-7 8-7s8 2 8 7z"/></svg>
      <h2 class="pillar__name">Adaptable</h2>
      <ul class="pillar__points">
        <li>Responds productively to new situations and feedback.</li>
        <li>Learns from experience and applies prior knowledge.</li>
        <li>Adjusts behavior to engage effectively in different settings.</li>
      </ul>
    </article>
    <article class="pillar">
      <svg class="pillar__icon" viewBox="0 0 56 56"><path d="M30 28c-10-7-14-11-14-16a7 7 0 0 1 14-2 7 7 0 0 1 14 2c0 5-4 9-14 16z"/><path d="M4 42l8-6c3-2 6-2 9 0h9c2 0 2 4 0 4h-8M31 40l13-6c3-1 5 2 2 4l-14 9H14l-6 3z"/></svg>
      <h2 class="pillar__name">Compassionate</h2>
      <ul class="pillar__points">
        <li>Understands and acknowledges others’ feelings.</li>
        <li>Responds with kindness, patience and support.</li>
        <li>Connects and contributes positively to community well-being.</li>
      </ul>
    </article>
    <article class="pillar">
      <svg class="pillar__icon" viewBox="0 0 56 56"><circle cx="17" cy="7" r="4"/><circle cx="28" cy="7" r="4"/><circle cx="39" cy="7" r="4"/><path d="M10 20c0-4 3-7 7-7s7 3 7 7M21 20c0-4 3-7 7-7s7 3 7 7M32 20c0-4 3-7 7-7s7 3 7 7"/><path d="M4 24l6-2 5 18-6 2zM52 24l-6-2-5 18 6 2z"/><path d="M14 26l8-2 6 3M42 26l-8-2-10 7c-2 2 1 4 3 3l5-3 7 7M16 38l6 6c2 1 4 0 4-2M20 36l7 7c2 1 4 0 4-2"/></svg>
      <h2 class="pillar__name">Collaborator</h2>
      <ul class="pillar__points">
        <li>Works cooperatively toward shared goals.</li>
        <li>Listens and values diverse ideas.</li>
        <li>Leads and compromises respectfully when needed.</li>
      </ul>
    </article>
  </section>

  <footer class="footer">
    <span class="footer__district">Corvath Falls Public Schools</span>
    <span class="footer__web">www.corvath.k12.example.us</span>
  </footer>
</main>
</body>
</html>
```